Wine Label named: Five Lanterns

We are a wine producer, who wishes to launch a new premium wine called: Five Lanterns
Our winery is situated in a rolling hill, with slopes, where Five Lanterns exists in the property. One dates to the 15th century and the other more recent to the 18th century. Its a unique feature of the winery and we wish to create a label that represents these, but is NOT religious! Difficult task I know. Think you can pull it off? Let us see it! We start with one label, but the winner will have 5 more labels to design.

Target Market(s)

30-50 year old men

Industry/Entity Type

Wine

Colors

Designer to choose colors to be used in the design.

Requirements
Must have
• serious look and premium feel. name of the wine: Five Lanterns
Nice to have
• 2019 14% ABV
Should not have
• a religious look and feel

```html
<!DOCTYPE html>
<html lang="en">
<head>
<meta charset="utf-8">
<title>Five Lanterns – Alentejo 2019 label</title>
<link rel="stylesheet" href="https://fonts.googleapis.com/css2?family=Bodoni+Moda:wght@400&family=Josefin+Sans:wght@400&display=swap">
<style>
  :root {
    --backdrop: #eceef2;
    --paper: #f7f7f5;
    --ink: #1d1b1b;
    --ember: #e0542a;
    --ember-deep: #d4481f;
    --band-text: #f6ddd0;
    --hill-soft: #f4d6c8;
    --hill-warm: #efb9a1;
  }
  * { margin: 0; padding: 0; box-sizing: border-box; }
  html, body {
    width: 1200px;
    height: 1077px;
    overflow: hidden;
    background: var(--backdrop);
  }
  .canvas {
    position: relative;
    width: 1200px;
    height: 1077px;
    display: flex;
    justify-content: space-around;
    align-items: center;
    padding: 0 60px;
  }
  .label {
    position: relative;
    width: 440px;
    height: 720px;
    background: var(--paper);
    box-shadow: 0 10px 30px rgba(40, 40, 50, 0.12);
    display: flex;
    flex-direction: column;
  }
  .label__face {
    position: relative;
    flex: 1 1 auto;
  }
  .label__band {
    flex: 0 0 210px;
    background: linear-gradient(90deg, var(--ember-deep), var(--ember) 55%, #e86a3f);
    display: flex;
    flex-direction: column;
    align-items: center;
    justify-content: center;
    gap: 36px;
    font-family: "Josefin Sans", sans-serif;
    color: var(--band-text);
  }
  .band__region {
    font-size: 15px;
    letter-spacing: 0.55em;
    margin-right: -0.55em;
  }
  .band__vintage {
    font-size: 16px;
    letter-spacing: 0.5em;
    margin-right: -0.5em;
  }
  .artwork {
    position: absolute;
    border-radius: 2px;
    background:
      radial-gradient(ellipse 70% 40% at 55% 40%, var(--hill-warm), transparent 70%),
      linear-gradient(160deg, var(--paper) 10%, var(--hill-soft) 45%, #ece8e4 80%);
  }
  .label--name-below .artwork { left: 26px; top: 60px; width: 390px; height: 370px; }
  .label--name-above .artwork { left: 26px; top: 140px; width: 390px; height: 340px; }

  .wine-name {
    position: absolute;
    left: 0;
    right: 0;
    text-align: center;
    white-space: nowrap;
    font-family: "Bodoni Moda", serif;
    font-weight: 400;
    font-style: normal;
    font-size: 32px;
    letter-spacing: 0.14em;
    text-indent: 0.14em;
    color: var(--ink);
    text-transform: uppercase;
    line-height: 1;
  }
  .label--name-below .wine-name { top: 452px; }
  .label--name-above .wine-name { top: 66px; }
</style>
</head>
<body>
<main class="canvas">
  <article class="label label--name-below">
    <div class="label__face">
      <div class="artwork" role="img" aria-label="Line drawing of two old buildings beneath orange hatched rolling hill slopes"></div>
      <h1 class="wine-name">Five Lanterns</h1>
    </div>
    <div class="label__band">
      <p class="band__region">ALENTEJO</p>
      <p class="band__vintage">2019</p>
    </div>
  </article>

  <article class="label label--name-above">
    <div class="label__face">
      <h1 class="wine-name">Five Lanterns</h1>
      <div class="artwork" role="img" aria-label="Line drawing of two old buildings beneath orange hatched rolling hill slopes"></div>
    </div>
    <div class="label__band">
      <p class="band__region">ALENTEJO</p>
      <p class="band__vintage">2019</p>
    </div>
  </article>
</main>
</body>
</html>
```